Exhibition Stand Design for innovative Social Business

We are an innovative social business empowering people to value nature through ZUN, a complementary digital currency. We have attached the TEK_ZUN branding document, and are needing a design for our exhibition stand (https://fairbuildlab.com/produit/stand-parapluie-classic-pvc-3x4c/. The attached doc mocks up a stand on page 32, though we would like some messaging included, in line with our website www.tekzun.ch. You will see there how the branding concept has been implemented with the TEK:GROW, SHARE, THRIVE wording, as well as all of us gain. Our green colours are included in the branding document. Many thanks!

Industry/Entity Type

Environment

Font styles to use
Other font styles liked:
• As per our attached fonts

Requirements
Must have
• Our attached branding guidelines gives our look and feel - Innovative / Dynamic / Vibrant / Reliable / Accessible / Connected.

```html
<!DOCTYPE html>
<html lang="en">
<head>
<meta charset="utf-8">
<title>TEKZUN – Exhibition Stand Graphics</title>
<link rel="stylesheet" href="https://fonts.googleapis.com/css2?family=Lexend:wght@500;600;700&display=swap">
<style>
  :root {
    --bg: #e9ebea;
    --green-mint: #43e3a6;
    --green-bright: #22e34c;
    --ink: #131a15;
    --light-text: #e4ece8;
    --bubble: rgba(255, 255, 255, 0.22);
  }
  * { box-sizing: border-box; margin: 0; padding: 0; }
  html, body {
    width: 1200px;
    height: 880px;
    overflow: hidden;
    background: var(--bg);
    font-family: "Lexend", sans-serif;
  }
  .stage {
    position: relative;
    width: 1200px;
    height: 880px;
  }

  /* Back wall graphic */
  .back-wall {
    position: absolute;
    left: 400px;
    top: 90px;
    width: 740px;
    height: 700px;
    overflow: hidden;
    background: linear-gradient(100deg, var(--green-mint) 0%, #36e27a 50%, var(--green-bright) 100%);
    color: var(--ink);
  }
  .bubble {
    position: absolute;
    border-radius: 50%;
    background: var(--bubble);
  }
  .bubble--top-right { width: 300px; height: 300px; right: -60px; top: -80px; }
  .bubble--bottom-left { width: 260px; height: 260px; left: -40px; bottom: -150px; }

  .brand-name {
    position: absolute;
    top: 112px;
    left: 0;
    width: 100%;
    text-align: center;
    font-weight: 600;
    font-size: 64px;
    letter-spacing: 1px;
    padding-right: 40px;
  }
  .tagline-small {
    position: absolute;
    top: 205px;
    left: 0;
    width: 100%;
    text-align: center;
    font-weight: 500;
    font-size: 22px;
    padding-right: 40px;
  }
  .pillars {
    position: absolute;
    top: 265px;
    left: 320px;
    list-style: none;
    font-weight: 500;
    font-size: 30px;
    line-height: 1.65;
  }
  .pillars__lead { color: var(--light-text); }
  .tagline-large {
    position: absolute;
    top: 528px;
    left: 0;
    width: 100%;
    text-align: center;
    font-weight: 500;
    font-size: 37px;
    padding-right: 40px;
  }
  .side-url {
    position: absolute;
    top: 0;
    height: 100%;
    display: flex;
    align-items: center;
    justify-content: center;
    font-weight: 700;
    font-size: 23px;
    letter-spacing: 1.5px;
    writing-mode: vertical-rl;
  }
  .side-url--left { left: 10px; transform: rotate(180deg); }
  .side-url--right { right: 12px; }

  /* Counter wrap graphic */
  .counter-wrap {
    position: absolute;
    left: 60px;
    top: 440px;
    width: 290px;
    height: 350px;
    background: linear-gradient(100deg, #47e3ad 0%, #3ee58a 100%);
    display: flex;
    align-items: center;
    justify-content: center;
    text-align: center;
  }
  .counter-wrap__slogan {
    color: var(--light-text);
    font-weight: 500;
    font-size: 44px;
    line-height: 1.2;
    margin-top: -40px;
  }
</style>
</head>
<body>
<main class="stage">
  <section class="back-wall" aria-label="Back wall graphic">
    <div class="bubble bubble--top-right"></div>
    <div class="bubble bubble--bottom-left"></div>
    <p class="side-url side-url--left">www.tekzun.ch</p>
    <p class="side-url side-url--right">www.tekzun.ch</p>
    <h1 class="brand-name">TEKZUN</h1>
    <p class="tagline-small">all of us gain</p>
    <ul class="pillars">
      <li class="pillars__lead">WE</li>
      <li>GROW</li>
      <li>SHARE</li>
      <li>THRIVE</li>
    </ul>
    <p class="tagline-large">all of us gain</p>
  </section>

  <section class="counter-wrap" aria-label="Counter wrap graphic">
    <p class="counter-wrap__slogan">all of us<br>gain</p>
  </section>
</main>
</body>
</html>
```